Creation of a Nutrition Consulting Flyer. For more information please see attached word document.

Industry/Entity Type

Health Service

Requirements
Must have
• Contend please see word document
The 3 fold flyer must meet the requirements of the DL formats, which is 210mm x 99 mm or for non 3 fold flyers DIN A 5 which is 210 mm x 148 mm (folded or non folded).
Nice to have
• our current idea is a 3 fold flyer but i am more than happy to receive other formats that better present the contend provided.

```html
<!DOCTYPE html>
<html lang="en">
<head>
<meta charset="utf-8">
<title>Nutrition Consulting Flyer</title>
<link href="https://fonts.googleapis.com/css2?family=Montserrat:wght@400;600;700;800&family=Open+Sans:wght@400;600&display=swap" rel="stylesheet">
<style>
  :root{
    --page:#f1f1f1;
    --panel:#e3e8ea;
    --panel-light:#edf1f2;
    --dark:#3a3633;
    --dark-2:#2f2c2a;
    --ink:#2f3234;
    --muted:#5d6366;
    --pill:#7b8184;
    --icon:#5a5f62;
    --white:#ffffff;
  }
  *{box-sizing:border-box;margin:0;padding:0}
  html,body{width:670px;height:1200px;overflow:hidden}
  body{background:var(--page);font-family:"Open Sans",Arial,sans-serif;color:var(--ink);position:relative}

  .spread{position:absolute;left:35px;width:600px;height:424px;display:flex;box-shadow:0 2px 10px rgba(0,0,0,.12)}
  .spread--outside{top:150px}
  .spread--inside{top:626px}
  .panel{width:200px;height:100%;position:relative;background:var(--panel);overflow:hidden}
  .panel--dark{background:linear-gradient(160deg,var(--dark),var(--dark-2));color:var(--white)}
  .panel--light{background:var(--panel-light)}

  .photo{position:absolute;left:0;width:100%}

  .brand{font-family:"Montserrat",Arial,sans-serif;font-weight:600;font-size:11px;letter-spacing:.6px;color:var(--ink)}
  .brand-sub{font-size:6px;color:var(--muted);margin-top:2px}
  .panel--dark .brand,.panel--dark .brand-sub{color:var(--white)}

  .heading{font-family:"Montserrat",Arial,sans-serif;font-weight:700;font-size:8px;line-height:1.35;text-transform:uppercase;color:var(--ink)}
  .body-text{font-size:5.6px;line-height:1.6;color:var(--muted);margin-top:7px}

  .aim{position:absolute;top:108px;left:16px;right:16px}

  .salad{position:absolute;top:24px;left:45px;width:110px;height:110px;border-radius:50%;border:4px solid var(--white);background:radial-gradient(circle at 45% 45%,#8fb85a,#4f7a2e 55%,#c9413a 80%,#f1eee6 92%)}
  .dark-brand{position:absolute;top:160px;left:0;right:0;text-align:center}
  .contact{position:absolute;top:230px;left:18px;right:18px}
  .contact-title{font-family:"Montserrat",Arial,sans-serif;font-weight:700;font-size:8px;letter-spacing:.5px}
  .contact-list{list-style:none;margin-top:10px}
  .contact-list li{display:flex;align-items:center;gap:7px;font-size:6px;margin-bottom:9px}
  .contact-list svg{flex:none}

  .cover-brand{position:absolute;top:16px;right:16px;text-align:left}
  .cover-title{position:absolute;top:58px;left:16px;right:12px;font-family:"Montserrat",Arial,sans-serif;font-weight:800;font-size:19px;line-height:1.15;color:var(--ink)}
  .pill{position:absolute;top:150px;left:16px;width:150px;height:14px;border-radius:7px;background:var(--pill);color:var(--white);font-size:6px;display:flex;align-items:center;justify-content:center;letter-spacing:.3px}

  .about{position:absolute;top:262px;left:16px;right:16px}
  .about-title{font-family:"Montserrat",Arial,sans-serif;font-weight:700;font-size:8px}
  .about-rule{width:150px;height:8px;border-radius:4px;background:var(--pill);margin-top:5px}

  .offer{position:absolute;top:18px;left:14px;right:12px}
  .offer-title{font-family:"Montserrat",Arial,sans-serif;font-weight:700;font-size:8px;letter-spacing:.3px}
  .offer-list{list-style:none;margin-top:12px}
  .offer-list li{display:flex;align-items:center;gap:8px;font-size:6px;line-height:1.35;margin-bottom:11px;color:var(--ink)}
  .offer-list .dot{flex:none;width:20px;height:20px;border-radius:50%;background:var(--icon);display:flex;align-items:center;justify-content:center}

  .info-brand{position:absolute;top:16px;left:16px}
  .info{position:absolute;top:62px;left:16px;right:14px}
  .info-title{font-family:"Montserrat",Arial,sans-serif;font-weight:700;font-size:8px}
  .info .body-text{margin-top:5px}
  .info-name{font-family:"Montserrat",Arial,sans-serif;font-weight:600;font-size:6.5px;margin-top:12px}
  .info .contact-list li{color:var(--ink);margin-bottom:6px;font-size:5.6px}
</style>
</head>
<body>

<!-- Outside spread -->
<section class="spread spread--outside">
  <div class="panel">
    <div class="photo" style="top:0;height:92px;background:linear-gradient(120deg,#cfd79a 0%,#e9ecec 40%,#e6eaec 70%,#3b4a78 100%)" role="img" aria-label="Fresh fruit and blueberries on a light surface"></div>
    <div class="aim">
      <h2 class="heading">My aim is to perfectly support you to achieve your aims</h2>
      <p class="body-text">Good food is the basis of a healthy life. Together we find a way of eating that fits your day and your goals.</p>
      <p class="body-text">I listen first, then we build a plan step by step, with simple meals and clear advice you can keep.</p>
      <p class="body-text">Whether you want more energy, better sleep or a lighter body, small changes make a real difference over time.</p>
    </div>
  </div>

  <div class="panel panel--dark">
    <div class="salad" role="img" aria-label="Bowl of fresh green salad with tomatoes"></div>
    <div class="dark-brand">
      <div class="brand">NUTRIVITA BLOG</div>
      <div class="brand-sub">Dr. Lena Hartmann</div>
    </div>
    <div class="contact">
      <div class="contact-title">CONTACT ME</div>
      <ul class="contact-list">
        <li><svg width="12" height="12" viewBox="0 0 12 12"><circle cx="6" cy="6" r="6" fill="#fff"/><path d="M4 3.2l1 1.3-.6.8c.4.8 1 1.4 1.8 1.8l.8-.6 1.3 1-.5 1.1C5.6 8.5 3.5 6.4 3.4 4z" fill="#3a3633"/></svg>+49 123 456 789</li>
        <li><svg width="12" height="12" viewBox="0 0 12 12"><circle cx="6" cy="6" r="6" fill="#fff"/><rect x="3" y="4" width="6" height="4.2" fill="none" stroke="#3a3633" stroke-width=".8"/><path d="M3 4l3 2.2L9 4" fill="none" stroke="#3a3633" stroke-width=".8"/></svg>hello@nutrivita.blog</li>
        <li><svg width="12" height="12" viewBox="0 0 12 12"><circle cx="6" cy="6" r="6" fill="#fff"/><circle cx="6" cy="6" r="3" fill="none" stroke="#3a3633" stroke-width=".8"/><path d="M3 6h6M6 3c-1.4 1.6-1.4 4.4 0 6M6 3c1.4 1.6 1.4 4.4 0 6" fill="none" stroke="#3a3633" stroke-width=".6"/></svg>www.nutrivita.blog</li>
      </ul>
    </div>
  </div>

  <div class="panel panel--light">
    <div class="cover-brand">
      <div class="brand">NUTRIVITA BLOG</div>
      <div class="brand-sub">Dr. Lena Hartmann</div>
    </div>
    <h1 class="cover-title">WELLBEING LIFE QUALITY HEALTH</h1>
    <div class="pill">www.nutrivita.blog</div>
    <div class="photo" style="bottom:0;height:220px;background:linear-gradient(160deg,#edf1f2 0%,#9fbf5a 35%,#5e8a2c 60%,#d9a070 80%,#edf1f2 100%)" role="img" aria-label="Broccoli, vegetables and nuts on a light table"></div>
  </div>
</section>

<!-- Inside spread -->
<section class="spread spread--inside">
  <div class="panel">
    <div class="photo" style="top:0;height:248px;background:linear-gradient(180deg,#dfe4e6 0%,#d8cbb8 45%,#f3f3f1 70%,#c7c9c8 100%)" role="img" aria-label="Nutrition consultant holding a bowl of salad"></div>
    <div class="about">
      <div class="about-title">ABOUT ME</div>
      <div class="about-rule"></div>
      <p class="body-text">I am a certified nutrition coach with over ten years of practice helping people eat well and feel better.</p>
      <p class="body-text">My approach is personal, practical and based on current science.</p>
    </div>
  </div>

  <div class="panel panel--light">
    <div class="offer">
      <div class="offer-title">I DEFINE YOU ON</div>
      <ul class="offer-list">
        <li><span class="dot"><svg width="10" height="10" viewBox="0 0 10 10"><path d="M2 5.2l2 2 4-4.4" fill="none" stroke="#fff" stroke-width="1.3"/></svg></span>Nutrition: devise a healthy diet</li>
        <li><span class="dot"><svg width="10" height="10" viewBox="0 0 10 10"><path d="M2 5.2l2 2 4-4.4" fill="none" stroke="#fff" stroke-width="1.3"/></svg></span>Your aim in new insights</li>
        <li><span class="dot"><svg width="10" height="10" viewBox="0 0 10 10"><path d="M2 5.2l2 2 4-4.4" fill="none" stroke="#fff" stroke-width="1.3"/></svg></span>Nutrition training programme</li>
        <li><span class="dot"><svg width="10" height="10" viewBox="0 0 10 10"><path d="M2 5.2l2 2 4-4.4" fill="none" stroke="#fff" stroke-width="1.3"/></svg></span>Nutrition during coaching</li>
        <li><span class="dot"><svg width="10" height="10" viewBox="0 0 10 10"><path d="M2 5.2l2 2 4-4.4" fill="none" stroke="#fff" stroke-width="1.3"/></svg></span>Preparation of healthful dishes for the whole family</li>
        <li><span class="dot"><svg width="10" height="10" viewBox="0 0 10 10"><path d="M2 5.2l2 2 4-4.4" fill="none" stroke="#fff" stroke-width="1.3"/></svg></span>Individual health</li>
      </ul>
    </div>
  </div>

  <div class="panel panel--light">
    <div class="info-brand">
      <div class="brand">NUTRIVITA BLOG</div>
      <div class="brand-sub">Dr. Lena Hartmann</div>
    </div>
    <div class="info">
      <div class="info-title">Information on my coaching offer</div>
      <p class="body-text">Book a first free call and we will talk about your needs and the right program for you.</p>
      <div class="info-name">Dr. Lena Hartmann</div>
      <ul class="contact-list">
        <li><svg width="10" height="10" viewBox="0 0 12 12"><circle cx="6" cy="6" r="6" fill="#5a5f62"/><path d="M4 3.2l1 1.3-.6.8c.4.8 1 1.4 1.8 1.8l.8-.6 1.3 1-.5 1.1C5.6 8.5 3.5 6.4 3.4 4z" fill="#fff"/></svg>+49 123 456 789</li>
        <li><svg width="10" height="10" viewBox="0 0 12 12"><circle cx="6" cy="6" r="6" fill="#5a5f62"/><rect x="3" y="4" width="6" height="4.2" fill="none" stroke="#fff" stroke-width=".8"/><path d="M3 4l3 2.2L9 4" fill="none" stroke="#fff" stroke-width=".8"/></svg>hello@nutrivita.blog</li>
        <li><svg width="10" height="10" viewBox="0 0 12 12"><circle cx="6" cy="6" r="6" fill="#5a5f62"/><circle cx="6" cy="6" r="3" fill="none" stroke="#fff" stroke-width=".8"/><path d="M3 6h6" stroke="#fff" stroke-width=".6"/></svg>www.nutrivita.blog</li>
      </ul>
    </div>
    <div class="photo" style="bottom:0;height:170px;background:linear-gradient(150deg,#edf1f2 0%,#c9a57a 35%,#8a6a48 60%,#e0d6c8 85%,#d6d8d8 100%)" role="img" aria-label="Bowl of granola with nuts and a spoon"></div>
  </div>
</section>

</body>
</html>
```